Interfaith Organization needs End of Year Mailing to Supporters

We need to mail out an end of the year appeal to our supporters highlighting our accomplishments and asking for their financial support. The project should be a mix of photos, text, and a space for mailing labels, a return address, and a stamp. We would like it to be 6x9, printed on both sides. We are an interfaith organization that works with students and religious leaders here in Los Angeles, CA.

Target Market(s)

supporters

Industry/Entity Type

Non-Profit

Font styles to use
Serif

Colors

Designer to choose colors to be used in the design.

Requirements
Must have
• an appealing mix of pictures, text, and space for mailing. The flyer should also feature the logos of our various programs.
Nice to have
• make it fun!
Should not have
• boring

```html
<!DOCTYPE html>
<html lang="en">
<head>
<meta charset="utf-8">
<title>Common Ground Circle – Year-End Appeal Mailer</title>
<link rel="stylesheet" href="https://fonts.googleapis.com/css2?family=Cinzel:wght@600;700&family=PT+Sans+Narrow:wght@400;700&display=swap">
<style>
  :root{
    --blue:#1f78c3;
    --blue-deep:#185f9e;
    --gold:#f2c230;
    --gold-soft:#e9c85a;
    --ink:#2b2b2b;
    --link:#1f6fb8;
    --paper:#ffffff;
    --stage:#ececec;
    --rule:#d6d6d6;
  }
  *{box-sizing:border-box;margin:0;padding:0}
  html,body{width:894px;height:1200px;overflow:hidden;background:var(--stage)}
  body{position:relative;font-family:"PT Sans Narrow",sans-serif;color:var(--ink)}
  .card{position:absolute;left:70px;width:756px;height:511px;background:var(--paper);overflow:hidden;box-shadow:0 2px 6px rgba(0,0,0,.18)}
  .card--front{top:50px}
  .card--back{top:636px}
  .abs{position:absolute}
  a,.link{color:var(--link);text-decoration:none}

  /* front header */
  .header-band{left:0;top:0;width:450px;height:142px}
  .header-kicker{left:34px;top:35px;font-family:"Cinzel",serif;font-weight:600;font-size:13.5px;color:#fff;letter-spacing:.3px}
  .header-title{left:34px;top:52px;font-family:"Cinzel",serif;font-weight:700;font-size:27px;line-height:28px;color:var(--gold);letter-spacing:.5px}
  .header-sub{left:34px;top:109px;font-family:"Cinzel",serif;font-weight:600;font-size:12.5px;color:#fff;letter-spacing:.3px}

  .photo{position:absolute;border:4px solid #fff;box-shadow:0 2px 5px rgba(0,0,0,.3)}
  .photo--city{left:430px;top:6px;width:158px;height:130px;transform:rotate(4deg);background:linear-gradient(180deg,#8fb4d8 0%,#c7d5df 45%,#7aa54a 70%,#4b6b3a 100%)}
  .photo--friends{left:603px;top:22px;width:150px;height:124px;transform:rotate(-6deg);background:linear-gradient(135deg,#c89a78,#7b5a48 55%,#e7dcd0)}
  .photo--temple{left:496px;top:134px;width:162px;height:134px;transform:rotate(3deg);background:linear-gradient(180deg,#9cc3e6 0%,#d9b790 40%,#a0795a 75%,#3f4a5e 100%)}
  .photo--sunset{left:452px;top:268px;width:304px;height:243px;background:radial-gradient(circle at 30% 40%,#ffd58a 0%,#f3a557 22%,#b98a6a 45%,#5e5a63 75%,#4d4c55 100%);-webkit-mask-image:linear-gradient(90deg,transparent 0%,#000 22%);mask-image:linear-gradient(90deg,transparent 0%,#000 22%)}

  .intro{left:32px;top:157px;width:382px;font-size:10.4px;line-height:14.8px}
  .program{position:absolute;font-size:10.4px;line-height:13.6px;padding-left:16px}
  .program::before{content:"";position:absolute;left:0;top:2px;width:9px;height:8px;background:var(--gold-soft);clip-path:polygon(50% 0,100% 50%,85% 50%,85% 100%,15% 100%,15% 50%,0 50%)}
  .fb-dot{display:inline-block;width:9px;height:9px;background:var(--blue);border-radius:1px;vertical-align:-1px}

  .rule{position:absolute;left:30px;width:424px;height:1px;background:var(--rule)}
  .brand{font-weight:700;color:var(--blue);font-size:20px;line-height:20px}
  .brand-mark{display:inline-block;width:22px;height:22px;border-radius:50%;border:2px solid var(--blue-deep);margin-left:6px;vertical-align:-4px}
  .vdivider{left:157px;top:366px;width:1px;height:50px;background:var(--rule)}
  .badge{position:absolute;top:369px;height:44px}
  .badge--one{left:177px;width:74px;background:linear-gradient(180deg,#3b5aa6,#26407f)}
  .badge--two{left:269px;width:58px;background:#3c3c3a;border-radius:2px}
  .badge--three{left:337px;width:93px;background:linear-gradient(180deg,#fff 30%,#9fd3ef 100%);border:1px solid #e2e2e2}

  .give-title{font-size:14px;line-height:15px;color:var(--ink)}
  .give-mail{font-size:10.5px;color:var(--link)}
  .sq{display:inline-block;width:14px;height:14px;background:var(--blue-deep);border-radius:2px;vertical-align:-2px;margin-right:6px}
  .social{font-size:10.4px;font-weight:700}
  .social i{display:inline-block;width:13px;height:13px;border-radius:50%;background:#2a9ee6;vertical-align:-3px;margin-right:5px}
  .social i.square{border-radius:3px;background:#e1306c}

  /* back */
  .sky{left:0;top:0;width:756px;height:280px;background:linear-gradient(180deg,#b9cde0 0%,#dbe6ef 45%,#eef2f6 70%,#ffffff 100%)}
  .back-copy{left:25px;top:25px;width:400px;font-size:10.3px;line-height:16px}
  .postage{left:674px;top:19px;width:62px;height:62px;border:1.5px solid #111;background:#fff;font-family:Arial,sans-serif;font-weight:700;font-size:9px;line-height:12px;text-align:center;padding-top:13px}
  .appeal-band{left:0;top:98px;width:431px;height:50px;background:var(--blue);border-radius:0 0 24px 0}
  .appeal-text{left:26px;top:110px;font-family:"Cinzel",serif;font-weight:700;font-size:10.8px;line-height:16px;color:var(--gold);letter-spacing:.2px}
  .phone{font-family:"Cinzel",serif;font-weight:700;font-size:19px;color:var(--ink)}
  .contact-line{font-size:12px}
  .send-head{font-size:12.5px}
  .address{font-size:12px;line-height:16px}
</style>
</head>
<body>

<section class="card card--front" aria-label="Mailer front">
  <svg class="abs header-band" viewBox="0 0 450 142" aria-hidden="true">
    <path d="M0 0H450V70C440 112 410 142 360 142H0Z" fill="var(--blue)"/>
  </svg>
  <div class="abs header-kicker">Common Ground Circle is in its</div>
  <div class="abs header-title">6th Year of Building<br>Interfaith Leaders</div>
  <div class="abs header-sub">Here in Los Angeles and Orange County.</div>

  <div class="photo photo--city" role="img" aria-label="Photo: youth group in green shirts in front of the downtown skyline"></div>
  <div class="photo photo--friends" role="img" aria-label="Photo: smiling students from different faiths"></div>
  <div class="photo photo--temple" role="img" aria-label="Photo: student group on the steps of a carved stone temple"></div>
  <div class="abs photo--sunset" role="img" aria-label="Photo: friends with arms around each other watching a sunset"></div>

  <p class="abs intro">Our vision is to work with high school and college youth of all religious traditions emphasizing community service, leadership development, and interfaith education. Common Ground Circle is offering a positive vision of engagement and needs your financial support. This past year we have worked with over 200 students with programs such as:</p>

  <div class="program" style="left:32px;top:229px">Youth Faith Council of Los Angeles County<br><span class="link">www.yfcla.example.org</span> | <span class="fb-dot"></span></div>
  <div class="program" style="left:32px;top:263px">Youth Bridge Leadership Initiatives –<br>Westmont Hills University, Harbor College,<br>Coastline State University<br><span class="link">www.ybli.example.org</span> | <span class="fb-dot"></span></div>
  <div class="program" style="left:32px;top:325px">Faith Forum and Festival</div>
  <div class="program" style="left:267px;top:229px">Youth Faith Council of Orange County<br><span class="link">www.yfcoc.example.org</span> | <span class="fb-dot"></span></div>
  <div class="program" style="left:267px;top:263px">Student Leadership Trips to Washington DC<br>and New Mexico</div>
  <div class="program" style="left:267px;top:297px">Shared Roots Peacemaking Initiative<br><span class="link">www.sharedrootspeace.example.org</span></div>

  <div class="rule" style="top:355px"></div>
  <div class="abs brand" style="left:38px;top:372px;width:110px">Common<br>Ground<span class="brand-mark"></span></div>
  <div class="abs vdivider"></div>
  <div class="badge badge--one" aria-hidden="true"></div>
  <div class="badge badge--two" aria-hidden="true"></div>
  <div class="badge badge--three" aria-hidden="true"></div>
  <div class="rule" style="top:428px"></div>

  <div class="abs" style="left:33px;top:446px"><span class="sq"></span><span class="give-title">Donate with GiveLink</span><br><span class="give-mail" style="margin-left:20px">give@commongroundcircle.org</span></div>
  <div class="abs social" style="left:230px;top:452px"><i></i>@CGCnews</div>
  <div class="abs social" style="left:342px;top:452px"><i class="square"></i>commongroundla</div>
</section>

<section class="card card--back" aria-label="Mailer back">
  <div class="abs sky" role="img" aria-label="Photo: soft sky above a sea of clouds"></div>
  <p class="abs back-copy">In addition, CGC also sponsors life-changing projects supporting survivors of genocide in Rwanda – <span class="link">www.hopehaven.example.org</span>, pre-school programs in Malawi – <span class="link">www.littlelearners.example.org</span>, a film project on a peace elder and forgiveness – <span class="link">www.forgivenessfilm.example.org</span> , and the Arroyo Learning Gardens – <span class="link">www.arroyogardens.example.org</span>. These projects serve over 2000 people each year!</p>
  <div class="abs brand" style="left:538px;top:30px;width:120px">Common<br>Ground<span class="brand-mark"></span></div>
  <div class="abs postage">POSTAGE<br>CLEAR<br>ZONE</div>

  <div class="abs appeal-band"></div>
  <div class="abs appeal-text">Will you help us meet our goal of $10,000 in individual<br>donations to help CGC sustain this needed work?</div>

  <div class="abs" style="left:25px;top:161px"><span class="sq"></span><span class="give-title">Donate with GiveLink</span><br><span class="give-mail" style="margin-left:20px">give@commongroundcircle.org</span></div>
  <div class="abs" style="left:25px;top:196px">
    <svg width="12" height="12" viewBox="0 0 24 24" aria-hidden="true" style="vertical-align:0"><path d="M6.6 10.8a15.1 15.1 0 0 0 6.6 6.6l2.2-2.2a1 1 0 0 1 1-.25 11.4 11.4 0 0 0 3.6.57 1 1 0 0 1 1 1V20a1 1 0 0 1-1 1A17 17 0 0 1 3 4a1 1 0 0 1 1-1h3.5a1 1 0 0 1 1 1c0 1.25.2 2.45.57 3.57a1 1 0 0 1-.25 1Z" fill="var(--blue)"/></svg>
    <span class="phone">(626) 555-0142</span>
  </div>
  <div class="abs contact-line" style="left:25px;top:230px">
    <svg width="11" height="11" viewBox="0 0 24 24" aria-hidden="true" style="vertical-align:-1px;margin-right:4px"><circle cx="12" cy="12" r="10" fill="none" stroke="var(--blue)" stroke-width="2"/><path d="M2 12h20M12 2c3 3 3 17 0 20M12 2c-3 3-3 17 0 20" fill="none" stroke="var(--blue)" stroke-width="1.6"/></svg>www.commongroundcircle.org
  </div>

  <div class="abs send-head" style="left:226px;top:164px">Or send your donation directly to:</div>
  <div class="abs address" style="left:226px;top:183px">
    <svg width="10" height="13" viewBox="0 0 24 32" aria-hidden="true" style="position:absolute;left:0;top:1px"><path d="M12 0a12 12 0 0 0-12 12c0 9 12 20 12 20s12-11 12-20A12 12 0 0 0 12 0Zm0 17a5 5 0 1 1 0-10 5 5 0 0 1 0 10Z" fill="var(--blue)"/></svg>
    <div style="padding-left:15px">Common Ground Circle<br>1480 E. Orchard Lane<br>Pasadena, CA&nbsp; 91100</div>
  </div>
</section>

</body>
</html>
```